Poster for our band

We need a logo and poster designing for us to send to the venues we are performing at. Our band is called "Drift"
Can use different backgrounds to make poster look more Arty
We would like the poster to look contemporary, modern and unique. As many or as little pictures can be used that I will send.
We perform at Holiday Parks, Hotels etc so the Poster needs to look classy and sophisticated.Can be Portrait or Landscape. Poster could be Black and White or Colour
A very creative Logo
Could contain the following script somewhere on the poster.

Performing hits by- The Hollow, Six Harbours, Mind Gap, Daniel Porter, Queens of Arlo, Runners, Q7, Marble Pilots and many more.

Poster needs our website address.
www.thegroupdrift.co.uk

Poster needs our Agent Name and number

Represented by- RBS - 01632 960418

Target Market(s)

Holiday Parks
Hotels
Nightclubs
Bars

Industry/Entity Type

Landscape

Colors
000000

Requirements
Must have
• Can be Portrait or Landscape. Poster could be Black and White or Colour
A very creative Logo

www.thegroupdrift.co.uk

Nice to have
• Cool, Contemopoary, Modern design
Photos can be cut out or changed in anyway to make us look great.

```html
<!DOCTYPE html>
<html lang="en">
<head>
<meta charset="utf-8">
<title>Drift — Poster</title>
<link rel="stylesheet" href="https://fonts.googleapis.com/css2?family=Signika:wght@400&display=swap">
<style>
  :root {
    --ink: #000000;
    --paper: #ffffff;
    --accent: #8dc63f;
  }
  * { margin: 0; padding: 0; box-sizing: border-box; }
  html, body {
    width: 848px;
    height: 1200px;
    overflow: hidden;
    background: var(--ink);
  }
  .poster {
    position: relative;
    width: 848px;
    height: 1200px;
    overflow: hidden;
    background: var(--ink);
    color: var(--paper);
    font-family: "Signika", "Trebuchet MS", sans-serif;
    font-weight: 400;
  }
  .band-name {
    font-weight: 400;
  }
  .band-name__line {
    position: absolute;
    display: flex;
    align-items: flex-end;
    font-size: 560px;
    line-height: 1;
    color: var(--paper);
    white-space: nowrap;
  }
  .band-name__line--top {
    left: 45px;
    top: -40px;
  }
  .band-name__line--bottom {
    left: 45px;
    top: 620px;
  }
  .band-name__mark {
    display: inline-block;
    width: 46px;
    height: 46px;
    margin: 0 0 132px 22px;
    background: var(--accent);
  }
  .setlist {
    position: absolute;
    left: 14px;
    bottom: 22px;
    width: 1140px;
    transform-origin: left bottom;
    transform: translateX(22px) rotate(-90deg);
    font-size: 19.5px;
    letter-spacing: 0.3px;
    white-space: nowrap;
  }
  .website {
    position: absolute;
    left: 252px;
    top: 564px;
    font-size: 30px;
    letter-spacing: 0.5px;
  }
  .agent {
    position: absolute;
    left: 655px;
    top: 886px;
    width: 180px;
    text-align: center;
    font-size: 19px;
    line-height: 28px;
    letter-spacing: 0.5px;
  }
</style>
</head>
<body>
  <main class="poster">
    <h1 class="band-name" aria-label="Drift">
      <span class="band-name__line band-name__line--top" aria-hidden="true">Dri</span>
      <span class="band-name__line band-name__line--bottom" aria-hidden="true">ft<span class="band-name__mark"></span></span>
    </h1>

    <p class="setlist">Performing hits by - The Hollow, Six Harbours, Mind Gap, Daniel Porter, Queens of Arlo, Runners, Q7, Marble Pilots and many more</p>

    <p class="website">www.thegroupdrift.co.uk</p>

    <p class="agent">Represented<br>by<br>- RBS -<br>01632 960418</p>
  </main>
</body>
</html>
```